Ledgivane - Corporate Overview - 2014

We need our Corporate Overview PPT for circulation to our clients urgently. We are an Accounting Outsourcing Company, having our Real Estate Funding arm based out of Goa, India.
I can share our draft PPT prepared in-house for further details.
The text may undergo a change, but need to make the PPT very insightful and corporate.
The designing should be based based out of our unique logo and should have our own identity.
Updates

Target Market(s)

REAL ESTATE COMPANIES requiring funding

Industry/Entity Type

Real Estate

Font styles to use
Serif

Requirements
Must have
• Real estate related high definition pictures
Nice to have
• Logo matching designs

```html
<!DOCTYPE html>
<html lang="en">
<head>
<meta charset="utf-8">
<title>Ledgivane – Corporate Overview 2014</title>
<link rel="stylesheet" href="https://fonts.googleapis.com/css2?family=Comfortaa:wght@400;700&family=Open+Sans:wght@400;600&family=Cinzel:wght@400;700&display=swap">
<style>
:root{
  --purple:#5b2d8e;
  --purple-dark:#44206f;
  --purple-soft:#b9a9d9;
  --purple-pale:#d9cfec;
  --ink:#4a3a63;
  --grey:#9a9a9a;
  --grey-light:#d6d6d6;
  --grey-pale:#eeeeee;
  --page:#e7e7e9;
  --white:#ffffff;
  --bokeh-deep:#0a2466;
  --bokeh-mid:#1f5fc8;
  --bokeh-warm:#c9a43e;
}
*{margin:0;padding:0;box-sizing:border-box}
html,body{width:1200px;height:1194px;overflow:hidden}
body{background:radial-gradient(circle at 50% 45%,#f1f1f3 0,var(--page) 70%);font-family:'Open Sans',sans-serif;position:relative}
.slide{position:absolute;background:linear-gradient(180deg,#fff 0,#f7f7f8 100%);overflow:hidden;box-shadow:0 1px 4px rgba(0,0,0,.12)}
.slide *{position:absolute}
.title{font:400 13px/1 'Comfortaa',sans-serif;color:var(--ink);left:12px;top:10px;white-space:nowrap}
.subtitle{font:400 5px/1 'Open Sans',sans-serif;color:#b5b5b5;left:12px;top:25px;white-space:nowrap}
.page-tag{top:0;right:4px;width:10px;height:24px;background:var(--purple);color:#fff;font:5px/10px 'Open Sans',sans-serif;writing-mode:vertical-rl;text-align:center}
.foot{left:0;right:0;bottom:5px;height:14px}
.brand{left:8px;top:0;height:14px;display:flex;align-items:center;gap:3px;position:absolute}
.brand *{position:static}
.brand-dot{width:11px;height:11px;border-radius:50%;background:#a9a9b2}
.brand-name{font:700 8px/1 'Comfortaa',sans-serif;color:var(--purple);letter-spacing:.2px}
.band{left:92px;right:24px;top:4px;height:7px;background:var(--purple-soft);color:#fff;font:4px/7px 'Open Sans',sans-serif;text-align:right;padding-right:4px}
.nav{right:4px;top:4px;width:18px;height:7px;background:var(--purple);color:#fff;font:700 5px/7px 'Open Sans',sans-serif;text-align:center;letter-spacing:2px}
.tiny{font:4.3px/1.5 'Open Sans',sans-serif;color:#9f9f9f}
.serif-cap{font:700 6px/1 'Cinzel',serif;color:var(--ink);letter-spacing:.3px}
.photo{display:block}

.cover-photo{inset:0;background:linear-gradient(180deg,#dfe9f2 0,#b8c8d8 35%,#7f95a8 58%,#5f7d5a 78%,#4c7a35 100%)}
.cover-logo{left:8px;top:14px;display:flex;align-items:center;gap:4px}
.cover-logo *{position:static}
.cover-logo .brand-dot{width:20px;height:20px}
.cover-logo .brand-name{font-size:12px}
.cover-band{left:0;top:144px;width:192px;height:28px;background:rgba(40,40,48,.85);color:#eee;font:400 15px/28px 'Comfortaa',sans-serif;padding-left:22px}
.cover-disc{left:246px;top:110px;width:190px;height:190px;border-radius:50%;background:rgba(255,255,255,.93)}
.cover-words{right:10px;top:138px;text-align:right;color:var(--purple);font:400 14px/1.25 'Comfortaa',sans-serif}
.cover-words b{display:block;position:static;font:400 23px/1.1 'Comfortaa',sans-serif;color:var(--purple-dark)}

.tower-photo{inset:0;background:linear-gradient(180deg,#7d8da2 0,#b7c2cf 40%,#e6ebf0 70%,#c7d0da 100%)}
.tower-head{left:0;right:0;top:0;height:46px;background:linear-gradient(180deg,#fff,rgba(255,255,255,.85))}
.tower-head .brand{top:8px;left:10px}
.tower-head .brand-dot{width:22px;height:22px}
.tower-head .brand-name{font-size:12px}
.tower-head .headline{right:10px;top:12px;font:400 14px/1 'Comfortaa',sans-serif;color:var(--purple-dark)}
.tower-band{left:0;right:0;top:166px;height:28px;background:rgba(108,60,170,.88);color:#efe9f7;text-align:center;font:400 15px/28px 'Comfortaa',sans-serif}

.bokeh{background:linear-gradient(135deg,var(--bokeh-deep) 0,var(--bokeh-mid) 55%,var(--bokeh-warm) 100%)}

.card{top:46px;width:80px;height:128px;background:#fff;border:1px solid #e6e6e6}
.card-head{left:0;right:0;top:0;height:12px;background:var(--purple);color:#fff;font:700 5px/12px 'Cinzel',serif;text-align:center;letter-spacing:.3px}
.card-icon{left:30px;top:22px;width:20px;height:20px}
.card-text{left:7px;right:7px;top:54px;text-align:center}
.card-btn{left:16px;right:16px;top:112px;height:9px;background:var(--purple-soft);color:#fff;font:700 3.8px/9px 'Cinzel',serif;text-align:center}

.row-icon{left:14px;width:14px;height:14px}
.row-text{left:40px;width:120px}
.cat{left:170px;font:3.8px/1 'Open Sans',sans-serif;color:#aaa}
.bar{left:203px;height:5px}
.bar.a{background:var(--purple)}
.bar.b{background:var(--grey-light)}
.axis-lbl{top:172px;font:3.8px/1 'Open Sans',sans-serif;color:#aaa}

.t-line{left:62px;top:56px;width:1px;height:112px;background:var(--grey-light)}
.t-dot{left:55px;width:15px;height:15px;border-radius:50%;background:#fff;border:1px solid var(--purple-soft)}
.t-dot i{left:3px;top:3px;width:7px;height:7px;border-radius:50%;background:var(--purple)}
.t-box{left:90px;width:230px;height:18px;border:1px solid #e4e4e4;background:#fff;padding:2px 4px}
.t-box span{position:static}

.member{top:44px;width:62px;height:140px}
.portrait{left:9px;top:4px;width:44px;height:44px;border-radius:50%;border:2px solid #fff;box-shadow:0 0 0 1px #ddd;background:linear-gradient(180deg,#e9e3dc,#c7b8a6 70%,#6b6f7d)}
.role{left:7px;top:0;width:13px;height:13px;border-radius:50%;background:var(--purple);color:#fff;font:3.5px/13px 'Open Sans',sans-serif;text-align:center}
.member .serif-cap{left:0;right:0;top:56px;text-align:center;font-size:5.5px}
.member .tiny{left:4px;right:0;top:64px}

.legend{font:3.8px/1.6 'Open Sans',sans-serif;color:#aaa}
.sw{display:inline-block;position:static;width:5px;height:3px;margin-right:2px;vertical-align:middle}

.ig-item{width:110px;height:24px}
.ig-icon{left:0;top:2px;width:18px;height:18px;border-radius:50%}
.ig-item .tiny{left:24px;top:0;width:86px}

.tbl{left:44px;top:64px;width:284px;border-collapse:collapse}
.tbl *{position:static}
.tbl th{font:400 5px/1 'Open Sans',sans-serif;color:var(--ink);padding:4px 0;border-top:1px solid var(--purple-soft);border-bottom:1px solid var(--purple-soft);text-align:center}
.tbl td{font:3.8px/1 'Open Sans',sans-serif;color:#aaa;height:19px;text-align:center;background:#e7e7e9}
.tbl tr:nth-child(even) td{background:#f4f4f5}

.label{font:3.8px/1.3 'Open Sans',sans-serif;color:#888}
.label-cap{font:400 4.5px/1 'Cinzel',serif;color:var(--purple)}

.thanks{left:14px;top:118px;font:400 24px/1 'Comfortaa',sans-serif;color:var(--purple-dark)}
.contact{left:20px;font:4.3px/1 'Open Sans',sans-serif;color:#888;display:flex;gap:8px;align-items:center}
.contact *{position:static}
.c-ico{width:6px;height:6px;border-radius:50%;background:var(--purple)}
.social{top:196px;width:8px;height:8px;background:var(--purple)}
</style>
</head>
<body>

<section class="slide" style="left:10px;top:24px;width:372px;height:212px">
  <div class="cover-photo photo" role="img" aria-label="Photo of a modern glass office building beside trees and a green lawn"></div>
  <div class="cover-logo"><span class="brand-dot"></span><span class="brand-name">LEDGIVANE</span></div>
  <div class="cover-band">Presentation Title</div>
  <div class="cover-disc"></div>
  <div class="cover-words">Corporate<br>Overview<b>2014</b></div>
</section>

<section class="slide" style="left:406px;top:24px;width:380px;height:214px">
  <div class="tower-photo photo" role="img" aria-label="Photo looking up at tall glass skyscrapers against the sky"></div>
  <div class="tower-head">
    <div class="brand"><span class="brand-dot"></span><span class="brand-name">LEDGIVANE</span></div>
    <div class="headline">Corporate Overview 2014</div>
  </div>
  <div class="tower-band">Presentation Title</div>
</section>

<section class="slide" style="left:811px;top:24px;width:380px;height:214px">
  <div class="title">Column Layout</div>
  <div class="subtitle">This is text place for second title</div>
  <div class="page-tag">PAGE 3</div>
  <div class="bokeh photo" style="left:40px;top:60px;width:83px;height:42px" role="img" aria-label="Photo of blue and gold out-of-focus city lights"></div>
  <div class="bokeh photo" style="left:147px;top:60px;width:83px;height:42px" role="img" aria-label="Photo of blue and gold out-of-focus city lights"></div>
  <div class="bokeh photo" style="left:254px;top:60px;width:83px;height:42px" role="img" aria-label="Photo of blue and gold out-of-focus city lights"></div>
  <p class="tiny" style="left:40px;top:108px;width:88px">This is sample copy for this column. Replace it with your own words about the firm, its services, clients and the value it brings in funding and accounts.</p>
  <p class="tiny" style="left:147px;top:108px;width:88px">This is sample copy for this column. Replace it with your own words about the firm, its services, clients and the value it brings in funding and accounts.</p>
  <p class="tiny" style="left:254px;top:108px;width:88px">This is sample copy for this column. Replace it with your own words about the firm, its services, clients and the value it brings in funding and accounts.</p>
  <div class="foot"><div class="brand"><span class="brand-dot"></span><span class="brand-name">LEDGIVANE</span></div><div class="band">www.yourwebsite.com</div><div class="nav">‹›</div></div>
</section>

<section class="slide" style="left:10px;top:256px;width:372px;height:210px">
  <div class="title">Product &amp; Services</div>
  <div class="subtitle">This is text place for second title</div>
  <div class="page-tag">PAGE 4</div>
  <div class="card" style="left:14px"><div class="card-head">LOREM IPSUM</div>
    <svg class="card-icon" viewBox="0 0 20 20"><circle cx="10" cy="8" r="5" fill="var(--purple)"/><rect x="8" y="13" width="4" height="4" fill="var(--purple)"/></svg>
    <p class="tiny card-text">Short sample copy describing this service line and what clients receive from it each month.</p><div class="card-btn">PRODUCT ONE</div></div>
  <div class="card" style="left:102px"><div class="card-head">LOREM IPSUM</div>
    <svg class="card-icon" viewBox="0 0 20 20"><circle cx="10" cy="11" r="7" fill="none" stroke="var(--purple)" stroke-width="2"/><path d="M10 7v4l3 2" stroke="var(--purple)" stroke-width="1.5" fill="none"/></svg>
    <p class="tiny card-text">Short sample copy describing this service line and what clients receive from it each month.</p><div class="card-btn">PRODUCT TWO</div></div>
  <div class="card" style="left:190px"><div class="card-head">LOREM IPSUM</div>
    <svg class="card-icon" viewBox="0 0 20 20"><path d="M2 9l5-4 3 3 3-3 5 4-8 7z" fill="var(--purple)"/></svg>
    <p class="tiny card-text">Short sample copy describing this service line and what clients receive from it each month.</p><div class="card-btn">PRODUCT THREE</div></div>
  <div class="card" style="left:278px"><div class="card-head">LOREM IPSUM</div>
    <svg class="card-icon" viewBox="0 0 20 20"><path d="M16 3c-5 0-9 4-10 9l3 3c5-1 9-5 9-10z M6 12l-3 5 5-3z" fill="var(--purple)"/></svg>
    <p class="tiny card-text">Short sample copy describing this service line and what clients receive from it each month.</p><div class="card-btn">PRODUCT FOUR</div></div>
  <div class="foot"><div class="brand"><span class="brand-dot"></span><span class="brand-name">LEDGIVANE</span></div><div class="band">www.yourwebsite.com</div><div class="nav">‹›</div></div>
</section>

<section class="slide" style="left:406px;top:256px;width:380px;height:212px">
  <div class="title">Bar Chart Layout</div>
  <div class="subtitle">This is text place for second title</div>
  <div class="page-tag">PAGE 5</div>
  <svg class="row-icon" style="top:56px" viewBox="0 0 14 14"><circle cx="7" cy="7" r="5" fill="none" stroke="var(--purple)" stroke-width="3" stroke-dasharray="2 1.5"/></svg>
  <svg class="row-icon" style="top:88px" viewBox="0 0 14 14"><path d="M2 2l10 10M12 2L2 12" stroke="var(--purple)" stroke-width="2"/></svg>
  <svg class="row-icon" style="top:120px" viewBox="0 0 14 14"><circle cx="7" cy="7" r="6" fill="none" stroke="var(--purple)"/><path d="M1 7h12M7 1v12" stroke="var(--purple)" stroke-width=".8"/></svg>
  <svg class="row-icon" style="top:152px" viewBox="0 0 14 14"><path d="M2 5h3l5-3v10l-5-3H2z" fill="var(--purple)"/></svg>
  <p class="tiny row-text" style="top:54px">Sample line of copy for this row, short and plain, to explain the figure shown.</p>
  <p class="tiny row-text" style="top:86px">Sample line of copy for this row, short and plain, to explain the figure shown.</p>
  <p class="tiny row-text" style="top:118px">Sample line of copy for this row, short and plain, to explain the figure shown.</p>
  <p class="tiny row-text" style="top:150px">Sample line of copy for this row, short and plain, to explain the figure shown.</p>
  <span class="cat" style="top:56px">Category 4</span>
  <div class="bar a" style="top:50px;width:74px"></div><div class="bar b" style="top:60px;width:143px"></div>
  <span class="cat" style="top:88px">Category 3</span>
  <div class="bar a" style="top:80px;width:153px"></div><div class="bar b" style="top:90px;width:80px"></div>
  <span class="cat" style="top:120px">Category 2</span>
  <div class="bar a" style="top:112px;width:54px"></div><div class="bar b" style="top:122px;width:118px"></div>
  <span class="cat" style="top:152px">Category 1</span>
  <div class="bar a" style="top:143px;width:54px"></div><div class="bar b" style="top:153px;width:134px"></div>
  <span class="axis-lbl" style="left:202px">0</span><span class="axis-lbl" style="left:229px">1</span><span class="axis-lbl" style="left:256px">2</span><span class="axis-lbl" style="left:283px">3</span><span class="axis-lbl" style="left:310px">4</span><span class="axis-lbl" style="left:337px">5</span><span class="axis-lbl" style="left:364px">6</span>
  <div class="foot"><div class="brand"><span class="brand-dot"></span><span class="brand-name">LEDGIVANE</span></div><div class="band">www.yourwebsite.com</div><div class="nav">‹›</div></div>
</section>

<section class="slide" style="left:811px;top:256px;width:380px;height:212px">
  <div class="title">Timeline Layout</div>
  <div class="subtitle">This is text place for second title</div>
  <div class="page-tag">PAGE 6</div>
  <div class="t-line"></div>
  <div class="t-dot" style="top:59px"><i></i></div>
  <div class="t-dot" style="top:90px"><i></i></div>
  <div class="t-dot" style="top:121px"><i></i></div>
  <div class="t-dot" style="top:152px"><i></i></div>
  <div class="t-box tiny" style="top:58px"><span>Milestone note in sample copy, a short and plain line about this stage of growth.</span></div>
  <div class="t-box tiny" style="top:89px"><span>Milestone note in sample copy, a short and plain line about this stage of growth.</span></div>
  <div class="t-box tiny" style="top:120px"><span>Milestone note in sample copy, a short and plain line about this stage of growth.</span></div>
  <div class="t-box tiny" style="top:151px"><span>Milestone note in sample copy, a short and plain line about this stage of growth.</span></div>
  <div class="foot"><div class="brand"><span class="brand-dot"></span><span class="brand-name">LEDGIVANE</span></div><div class="band">www.yourwebsite.com</div><div class="nav">‹›</div></div>
</section>

<section class="slide" style="left:10px;top:488px;width:372px;height:206px">
  <div class="title">Our Team</div>
  <div class="subtitle">This is text place for second title</div>
  <div class="page-tag">PAGE 7</div>
  <div class="member" style="left:54px"><div class="portrait photo" role="img" aria-label="Portrait photo of a team member"></div><div class="role">CEO</div><div class="serif-cap">LOREM IPSUM</div><p class="tiny">• A short note on this role and the work it leads.<br><br>• Years in practice and key skills.</p></div>
  <div class="member" style="left:122px"><div class="portrait photo" role="img" aria-label="Portrait photo of a team member"></div><div class="role">VM</div><div class="serif-cap">LOREM IPSUM</div><p class="tiny">• A short note on this role and the work it leads.<br><br>• Years in practice and key skills.</p></div>
  <div class="member" style="left:190px"><div class="portrait photo" role="img" aria-label="Portrait photo of a team member"></div><div class="role">VP</div><div class="serif-cap">LOREM IPSUM</div><p class="tiny">• A short note on this role and the work it leads.<br><br>• Years in practice and key skills.</p></div>
  <div class="member" style="left:256px"><div class="portrait photo" role="img" aria-label="Portrait photo of a team member"></div><div class="role">PR</div><div class="serif-cap">LOREM IPSUM</div><p class="tiny">• A short note on this role and the work it leads.<br><br>• Years in practice and key skills.</p></div>
  <div class="foot"><div class="brand"><span class="brand-dot"></span><span class="brand-name">LEDGIVANE</span></div><div class="band">www.yourwebsite.com</div><div class="nav">‹›</div></div>
</section>

<section class="slide" style="left:406px;top:490px;width:380px;height:208px">
  <div class="bokeh photo" style="left:8px;top:3px;width:140px;height:205px" role="img" aria-label="Photo of blue and gold out-of-focus lights"></div>
  <div class="page-tag">PAGE 8</div>
  <div class="title" style="left:198px;top:46px;font-size:12px">Image &amp; Texts</div>
  <div class="subtitle" style="left:198px;top:60px">text for second title</div>
  <p class="tiny" style="left:198px;top:76px;width:165px">This is sample copy for a text block beside a full image. It speaks about the firm, its history in accounts outsourcing and its funding arm for real estate clients. Keep lines short and clear so each idea reads at a glance on screen and in print for all readers.</p>
  <p class="tiny" style="left:198px;top:128px;width:165px">This is sample copy for a text block beside a full image. It speaks about the firm, its history in accounts outsourcing and its funding arm for real estate clients. Keep lines short and clear so each idea reads at a glance on screen and in print for all readers.</p>
  <div class="foot"><div class="band" style="left:160px">www.yourwebsite.com</div><div class="nav">‹›</div></div>
</section>

<section class="slide" style="left:811px;top:490px;width:380px;height:208px">
  <div class="title">Video Layout</div>
  <div class="subtitle">This is text place for second title</div>
  <div class="page-tag">PAGE 9</div>
  <div class="photo" style="left:35px;top:42px;width:187px;height:126px;border-radius:5px;background:linear-gradient(160deg,#3a3a3e,#121214 60%,#2a2a2d)" role="img" aria-label="Laptop showing a video player"></div>
  <div style="left:14px;top:168px;width:230px;height:5px;border-radius:0 0 6px 6px;background:linear-gradient(#d8d8da,#a9a9ac)"></div>
  <svg style="left:116px;top:96px;width:20px;height:16px" viewBox="0 0 20 16"><path d="M6 2l10 6-10 6z" fill="#555"/></svg>
  <div style="left:251px;top:58px;font:400 11px/1 'Comfortaa',sans-serif;color:var(--purple)">LOREM IPSUM</div>
  <p class="tiny" style="left:251px;top:72px;width:112px;color:#8a7aa8;font-size:4.8px">Sample copy for the video panel. Tell clients what the clip covers, who speaks in it and why it matters to the funding plans they hold today. Keep it short and plain for quick reading. Add a line on length and the key point of the talk so viewers know what comes next.</p>
  <div class="foot"><div class="brand"><span class="brand-dot"></span><span class="brand-name">LEDGIVANE</span></div><div class="band">www.yourwebsite.com</div><div class="nav">‹›</div></div>
</section>

<section class="slide" style="left:10px;top:720px;width:372px;height:206px">
  <div class="title">Graphic Chart Layout</div>
  <div class="subtitle">This is text place for second title</div>
  <div class="page-tag">PAGE 10</div>
  <p class="tiny" style="left:42px;top:34px;width:312px;font-size:5.3px">Sample copy above the chart, a plain note that sets out what the figures show and where they come from, written to fill two short lines of text.</p>
  <svg style="left:40px;top:58px;width:270px;height:96px" viewBox="0 0 270 96">
    <g stroke="#e4e4e4" stroke-width=".5"><path d="M8 6h240M8 21h240M8 36h240M8 51h240M8 66h240M8 81h240"/></g>
    <g fill="var(--purple)"><rect x="28" y="8" width="11" height="73"/><rect x="85" y="51" width="11" height="30"/><rect x="142" y="20" width="11" height="61"/><rect x="201" y="8" width="11" height="73"/></g>
    <g fill="var(--purple-soft)"><rect x="40" y="54" width="11" height="27"/><rect x="97" y="6" width="11" height="75"/><rect x="154" y="56" width="11" height="25"/><rect x="213" y="35" width="11" height="46"/></g>
    <g fill="var(--grey-light)"><rect x="52" y="61" width="11" height="20"/><rect x="109" y="61" width="11" height="20"/><rect x="166" y="36" width="11" height="45"/><rect x="225" y="66" width="11" height="15"/></g>
    <g font-family="Open Sans" font-size="3.8" fill="#aaa"><text x="36" y="90">Category 1</text><text x="94" y="90">Category 2</text><text x="152" y="90">Category 3</text><text x="210" y="90">Category 4</text></g>
  </svg>
  <div class="legend" style="left:306px;top:86px"><span class="sw" style="background:var(--purple)"></span>Series 1<br><span class="sw" style="background:var(--purple-soft)"></span>Series 2<br><span class="sw" style="background:var(--grey-light)"></span>Series 3</div>
  <div style="left:44px;top:158px;width:10px;height:10px;border-radius:50%;background:var(--purple)"></div>
  <div class="serif-cap" style="left:62px;top:160px;font-weight:400">LOREM IPSUM</div>
  <p class="tiny" style="left:40px;top:171px;width:305px">Sample note under the chart, one plain line to say what the series mean and a second line for the source.</p>
  <div class="foot"><div class="brand"><span class="brand-dot"></span><span class="brand-name">LEDGIVANE</span></div><div class="band">www.yourwebsite.com</div><div class="nav">‹›</div></div>
</section>

<section class="slide" style="left:406px;top:726px;width:380px;height:208px">
  <div class="title">Graphic Chart Layout</div>
  <div class="subtitle">This is text place for second title</div>
  <div class="page-tag">PAGE 11</div>
  <p class="tiny" style="left:38px;top:40px;width:320px;font-size:5.3px">Sample copy above the chart, a plain note that sets out what the figures show and where they come from, written to fill two short lines of text.</p>
  <svg style="left:36px;top:70px;width:280px;height:80px" viewBox="0 0 280 80">
    <g stroke="#e4e4e4" stroke-width=".5"><path d="M10 6h260M10 20h260M10 34h260M10 48h260M10 62h260"/></g>
    <polygon points="14,62 14,30 95,48 185,20 268,30 268,62" fill="var(--purple-pale)"/>
    <polygon points="14,62 14,10 95,30 185,30 268,2 268,62" fill="var(--purple)" opacity=".95"/>
    <polygon points="14,62 14,40 95,10 185,46 268,24 268,62" fill="var(--purple-soft)"/>
    <polygon points="14,62 14,46 95,36 185,42 268,52 268,62" fill="#cfcfd2"/>
    <g font-family="Open Sans" font-size="3.8" fill="#aaa"><text x="10" y="74">Category 1</text><text x="90" y="74">Category 2</text><text x="180" y="74">Category 3</text><text x="255" y="74">Category 4</text></g>
  </svg>
  <div class="legend" style="left:320px;top:88px"><span class="sw" style="background:var(--purple)"></span>Series 1<br><span class="sw" style="background:var(--purple-soft)"></span>Series 2<br><span class="sw" style="background:#cfcfd2"></span>Series 3</div>
  <div style="left:40px;top:158px;width:10px;height:10px;border-radius:50%;background:#f1b51c"></div>
  <div class="serif-cap" style="left:58px;top:160px;font-weight:400">LOREM IPSUM</div>
  <p class="tiny" style="left:36px;top:171px;width:310px">Sample note under the chart, one plain line to say what the series mean and a second line for the source.</p>
  <div class="foot"><div class="brand"><span class="brand-dot"></span><span class="brand-name">LEDGIVANE</span></div><div class="band">www.yourwebsite.com</div><div class="nav">‹›</div></div>
</section>

<section class="slide" style="left:811px;top:716px;width:380px;height:212px">
  <div class="title">Icon Layout</div>
  <div class="subtitle">This is text place for second title</div>
  <div class="page-tag">PAGE 12</div>
  <div class="ig-item" style="left:14px;top:68px"><div class="ig-icon" style="background:var(--purple)"></div><p class="tiny">Sample line for this icon, kept short and plain to fit.</p></div>
  <div class="ig-item" style="left:134px;top:68px"><div class="ig-icon" style="background:var(--purple)"></div><p class="tiny">Sample line for this icon, kept short and plain to fit.</p></div>
  <div class="ig-item" style="left:252px;top:68px"><div class="ig-icon" style="background:var(--purple)"></div><p class="tiny">Sample line for this icon, kept short and plain to fit.</p></div>
  <div class="ig-item" style="left:14px;top:101px"><div class="ig-icon" style="background:var(--purple-soft)"></div><p class="tiny">Sample line for this icon, kept short and plain to fit.</p></div>
  <div class="ig-item" style="left:134px;top:101px"><div class="ig-icon" style="background:var(--purple-soft)"></div><p class="tiny">Sample line for this icon, kept short and plain to fit.</p></div>
  <div class="ig-item" style="left:252px;top:101px"><div class="ig-icon" style="background:var(--purple-soft)"></div><p class="tiny">Sample line for this icon, kept short and plain to fit.</p></div>
  <div class="ig-item" style="left:14px;top:134px"><div class="ig-icon" style="background:#777"></div><p class="tiny">Sample line for this icon, kept short and plain to fit.</p></div>
  <div class="ig-item" style="left:134px;top:134px"><div class="ig-icon" style="background:#777"></div><p class="tiny">Sample line for this icon, kept short and plain to fit.</p></div>
  <div class="ig-item" style="left:252px;top:134px"><div class="ig-icon" style="background:#777"></div><p class="tiny">Sample line for this icon, kept short and plain to fit.</p></div>
  <div class="foot"><div class="brand"><span class="brand-dot"></span><span class="brand-name">LEDGIVANE</span></div><div class="band">www.yourwebsite.com</div><div class="nav">‹›</div></div>
</section>

<section class="slide" style="left:10px;top:946px;width:372px;height:208px">
  <div class="title">Table Layout</div>
  <div class="subtitle">This is text place for second title</div>
  <div class="page-tag">PAGE 13</div>
  <p class="tiny" style="left:34px;top:40px;width:310px">Sample copy above the table, a plain note that sets out what the rows hold, written to fill two short lines.</p>
  <table class="tbl">
    <tr><th>LOREM IPSUM</th><th>LOREM IPSUM</th><th>LOREM IPSUM</th><th>LOREM IPSUM</th></tr>
    <tr><td>Lorem ipsum</td><td>Lorem ipsum</td><td>Lorem ipsum</td><td>Lorem ipsum</td></tr>
    <tr><td>Lorem ipsum</td><td>Lorem ipsum</td><td>Lorem ipsum</td><td>Lorem ipsum</td></tr>
    <tr><td>Lorem ipsum</td><td>Lorem ipsum</td><td>Lorem ipsum</td><td>Lorem ipsum</td></tr>
    <tr><td>Lorem ipsum</td><td>Lorem ipsum</td><td>Lorem ipsum</td><td>Lorem ipsum</td></tr>
    <tr><td>Lorem ipsum</td><td>Lorem ipsum</td><td>Lorem ipsum</td><td>Lorem ipsum</td></tr>
  </table>
  <div class="foot"><div class="brand"><span class="brand-dot"></span><span class="brand-name">LEDGIVANE</span></div><div class="band">www.yourwebsite.com</div><div class="nav">‹›</div></div>
</section>

<section class="slide" style="left:406px;top:946px;width:380px;height:212px">
  <div class="title">Process Layout</div>
  <div class="subtitle">This is text place for second title</div>
  <div class="page-tag">PAGE 14</div>
  <svg style="left:80px;top:40px;width:240px;height:140px" viewBox="0 0 240 140">
    <path d="M15 122 C45 60 110 40 190 28 L185 12 L230 40 L195 70 L192 50 C120 55 60 80 15 122Z" fill="var(--purple-pale)"/>
    <path d="M15 122 C50 75 110 52 190 40" fill="none" stroke="var(--purple)" stroke-width=".6"/>
    <circle cx="15" cy="122" r="2" fill="var(--purple)"/>
    <circle cx="50" cy="89" r="5" fill="var(--purple)"/>
    <circle cx="95" cy="62" r="6" fill="var(--purple)"/>
    <circle cx="150" cy="45" r="8" fill="var(--purple)"/>
    <circle cx="220" cy="30" r="15" fill="var(--purple)"/>
    <path d="M226 22c-6 0-10 4-11 10l3 3c6-1 10-5 10-11z" fill="#fff"/>
  </svg>
  <div style="left:290px;top:90px;font:400 10px/1 'Comfortaa',sans-serif;color:var(--purple)">SUCCESS</div>
  <span class="label-cap" style="left:100px;top:170px">LOREM IPSUM</span>
  <span class="label-cap" style="left:124px;top:142px">LOREM IPSUM</span>
  <span class="label-cap" style="left:162px;top:120px">LOREM IPSUM</span>
  <span class="label-cap" style="left:220px;top:105px">LOREM IPSUM</span>
  <p class="label" style="left:40px;top:125px;width:40px">Short sample step note here.</p>
  <p class="label" style="left:72px;top:90px;width:40px">Short sample step note here.</p>
  <p class="label" style="left:118px;top:54px;width:40px">Short sample step note here.</p>
  <p class="label" style="left:216px;top:130px;width:40px">Short sample step note here.</p>
  <div class="foot"><div class="brand"><span class="brand-dot"></span><span class="brand-name">LEDGIVANE</span></div><div class="band">www.yourwebsite.com</div><div class="nav">‹›</div></div>
</section>

<section class="slide" style="left:811px;top:944px;width:380px;height:214px">
  <div class="thanks">THANK YOU</div>
  <div style="left:14px;top:146px;width:100px;height:1px;background:var(--purple-soft)"></div>
  <div class="contact" style="top:152px"><span class="c-ico"></span>000-000-0000</div>
  <div class="contact" style="top:165px"><span class="c-ico"></span>xyz@email.com</div>
  <div class="contact" style="top:178px"><span class="c-ico"></span>www.yourwebsite.com</div>
  <div style="left:14px;top:190px;width:102px;height:1px;background:var(--grey-light)"></div>
  <div class="social" style="left:18px"></div>
  <div class="social" style="left:32px"></div>
  <div class="social" style="left:46px"></div>
</section>

</body>
</html>
```